BRIX Rentals ( Website Graphic design ) small property management new business ( real estate )

I need a website designed for a new small Property Management ( no sales ) company I'm starting up soon. I have a design in mind that I like and would like to keep it quite similar to this if possible using my logo and colour scheme and slightly ALTER the layout. and maybe a little more interactive with some motion and images etc
Please see the link to show the simplicity I'm after. I want to be bold ad very clear and concise. I love the simplicity of this design but not necessarily the pages with just text on them. I would want them to be a bit more interesting with some pictures and photos. http://www.lindavostrel.com.au/

The branding on the site should be bold and very sharp.

My target market is the mid to high end of the rental market in Darwin Australia and should reflect "good quality, outstanding service and attention to detail, energetic, integrity, "

I will only require a few pages to start with, Home / Company Profile / Management Services / Owners information / Tenant information / Properties and About Darwin. I will be able to provide text for each of the pages but would be no more than 4-6 paragraphs apart from the management services page which would detail a number of the services we would offer. The properties page will just be a link to homelistz,com.au to show my listings and then a couple more links to owner and tenant portals, chatterbox page etc. It must also be responsive to mobile devices.

I would also like to include a chatterbox page design and build.

regards
Marta Penhale

Target Market(s)

property owners, investors, Darwin Australia, renters, ages 30 - 60, tenants

Industry/Entity Type

Property Management

Font styles to use
Other font styles liked:
• i like helvetica, but not essential

Requirements
Must have
• Clean and crisp pages, not busy , responsive to devices
• links to portals and chatterbox, any ability to add other links at a later date.
Nice to have
• music - must be upbeat but not over the top
Should not have
• be too busy on each page

```html
<!DOCTYPE html>
<html lang="en">
<head>
<meta charset="utf-8">
<title>BRIX Rentals — Home</title>
<link rel="stylesheet" href="https://fonts.googleapis.com/css2?family=Open+Sans:wght@300;400&display=swap">
<style>
  :root {
    --teal: #008a8e;
    --charcoal: #4a4647;
    --white: #ffffff;
    --tile: 217px;
    --step: 231px;
  }
  * { box-sizing: border-box; margin: 0; padding: 0; }
  html, body { width: 1200px; height: 893px; overflow: hidden; }
  body {
    background: var(--teal);
    font-family: "Open Sans", Helvetica, Arial, sans-serif;
    position: relative;
  }
  .tile-grid {
    position: absolute;
    left: 167.5px;
    top: 135px;
    transform-origin: 0 0;
    transform: rotate(-32deg);
  }
  .tile {
    position: absolute;
    width: var(--tile);
    height: var(--tile);
    display: block;
    text-decoration: none;
  }
  .tile--dark { background: var(--charcoal); color: var(--white); }
  .tile--light { background: var(--white); color: var(--teal); }

  .tile--brand   { left: 0; top: 0; }
  .tile--profile { left: 0; top: var(--step); }
  .tile--services{ left: var(--step); top: var(--step); }
  .tile--owners  { left: calc(var(--step) * 2); top: var(--step); }
  .tile--props   { left: 0; top: calc(var(--step) * 2); }
  .tile--tenant  { left: var(--step); top: calc(var(--step) * 2); }
  .tile--darwin  { left: calc(var(--step) * -1); top: calc(var(--step) * 2); }

  .tile--dark .tile__content {
    position: absolute;
    left: 12px;
    bottom: 12px;
    display: flex;
    flex-direction: column;
    align-items: flex-start;
    gap: 4px;
  }
  .tile__icon { width: 46px; height: 42px; fill: currentColor; }
  .tile__label { font-size: 15.5px; font-weight: 400; letter-spacing: 0.2px; white-space: nowrap; }

  .tile--light .tile__label {
    position: absolute;
    left: 12px;
    top: 13px;
    writing-mode: vertical-rl;
  }
  .tile--light .tile__icon {
    position: absolute;
    left: 42px;
    top: 14px;
    width: 46px;
    height: 46px;
  }

  .brand-name {
    position: absolute;
    left: 250px;
    top: 78px;
    color: var(--white);
    font-weight: 300;
    line-height: 1;
  }
  .brand-name__main { display: block; font-size: 56px; letter-spacing: -1px; }
  .brand-name__sub { display: block; font-size: 34px; margin: 10px 0 0 -14px; }
</style>
</head>
<body>
  <nav class="tile-grid" aria-label="Main">
    <div class="tile tile--dark tile--brand"></div>

    <a class="tile tile--dark tile--profile" href="#profile">
      <span class="tile__content">
        <svg class="tile__icon" viewBox="0 0 46 42" aria-hidden="true">
          <path d="M3 10h12l4 4h20v4H11L3 38z"/>
          <path d="M12 20h33l-8 20H4z"/>
        </svg>
        <span class="tile__label">Company Profile</span>
      </span>
    </a>

    <a class="tile tile--light tile--services" href="#services">
      <span class="tile__label">Management Services</span>
      <svg class="tile__icon" viewBox="0 0 46 46" aria-hidden="true">
        <path d="M6 6h34v26H6zM9 9v20h28V9z"/>
        <path d="M4 36h38v4H4z"/>
        <path d="M13 12l3-3 17 17-3 3z"/>
        <path d="M30 10a5 5 0 1 0 5 6l-3-1-1-3z"/>
        <path d="M14 26l9-9 2 2-9 9z"/>
      </svg>
    </a>

    <a class="tile tile--light tile--owners" href="#owners">
      <span class="tile__label">Owners information</span>
      <svg class="tile__icon" viewBox="0 0 46 46" aria-hidden="true">
        <path d="M4 4h22l6 6v20H4zM8 12h18v2H8zm0 5h18v2H8zm0 5h18v2H8z"/>
        <circle cx="36" cy="22" r="4"/>
        <path d="M31 28h10v8h-3v8h-4v-8h-3z"/>
      </svg>
    </a>

    <a class="tile tile--light tile--props" href="#properties">
      <span class="tile__label">Properties</span>
      <svg class="tile__icon" viewBox="0 0 46 46" aria-hidden="true">
        <path d="M4 6h26v36H4zM8 10v4h4v-4zm6 0v4h4v-4zm6 0v4h4v-4zM8 17v4h4v-4zm6 0v4h4v-4zm6 0v4h4v-4zM8 24v4h4v-4zm6 0v4h4v-4zm6 0v4h4v-4zM14 34v8h6v-8z"/>
        <path d="M32 16h10v26H32zM35 20v3h4v-3zm0 6v3h4v-3zm0 6v3h4v-3z"/>
      </svg>
    </a>

    <a class="tile tile--dark tile--tenant" href="#tenants">
      <span class="tile__content">
        <svg class="tile__icon" viewBox="0 0 46 42" aria-hidden="true">
          <path d="M32 4a11 11 0 1 1-9 17L8 30v4H4v-4H2v-5l18-10A11 11 0 0 1 32 4zm0 5a5 5 0 1 0 0 10 5 5 0 0 0 0-10z"/>
        </svg>
        <span class="tile__label">Tenant information</span>
      </span>
    </a>

    <a class="tile tile--dark tile--darwin" href="#darwin">
      <span class="tile__content">
        <svg class="tile__icon" viewBox="0 0 46 42" aria-hidden="true">
          <ellipse cx="23" cy="12" rx="8" ry="10"/>
          <path d="M6 40c0-9 7-14 17-14s17 5 17 14z"/>
        </svg>
        <span class="tile__label">About Darwin</span>
      </span>
    </a>
  </nav>

  <h1 class="brand-name">
    <span class="brand-name__main">BRIX</span>
    <span class="brand-name__sub">Rentals</span>
  </h1>
</body>
</html>
```